Civil engineering company | Billboard

We need a billboard design for Velmora- civil engineering company. We want big logo in the center of billboard and web site (www.velmora.hr) below the logo. Also, we want an subtle abstract pattern in the background. Dimensions of the billboard are: width :10 m, height: 2m. Design must be celan and modern.
Industry/Entity Type
Civil engineering
Font styles to use
Sans Serif
Colors
F0912C
F2A743
F7CA91
FBE8D2
FDF5EE
Requirements
Must have
- Logo and new unique pattern design for Velmroa company
Should not have
- pictures of construction machinery and tools

```html
<!DOCTYPE html>
<html lang="hr">
<head>
<meta charset="utf-8">
<title>Velmora – billboard</title>
<link rel="stylesheet" href="https://fonts.googleapis.com/css2?family=Montserrat:wght@500;600&family=Poppins:wght@600&display=swap">
<style>
  :root {
    --orange-deep: #F0912C;
    --orange: #F2A743;
    --orange-soft: #F7CA91;
    --cream: #FBE8D2;
    --paper: #FDF5EE;
    --white: #FFFFFF;
    --ink: #1E1B18;
    --grey: #5E5E5E;
    --stage: #BEBEBE;
  }
  * { margin: 0; padding: 0; box-sizing: border-box; }
  html, body {
    width: 1128px;
    height: 1200px;
    overflow: hidden;
    background: var(--stage);
  }
  .canvas {
    position: relative;
    width: 1128px;
    height: 1200px;
  }
  .billboard {
    position: absolute;
    left: 44px;
    top: 496px;
    width: 1040px;
    height: 208px;
    background: var(--white);
    overflow: hidden;
    box-shadow: 0 10px 14px rgba(0, 0, 0, 0.35);
  }
  .billboard__bands {
    position: absolute;
    inset: 0;
    width: 100%;
    height: 100%;
  }
  .brand {
    position: absolute;
    left: 0;
    right: 0;
    top: 44px;
    display: flex;
    flex-direction: column;
    align-items: center;
  }
  .brand__row {
    display: flex;
    align-items: center;
    gap: 12px;
  }
  .brand__square {
    width: 26px;
    height: 26px;
    background: var(--orange-deep);
  }
  .brand__name {
    font-family: "Montserrat", sans-serif;
    font-weight: 500;
    font-size: 40px;
    letter-spacing: 1px;
    line-height: 1;
    color: var(--orange-deep);
  }
  .brand__tagline {
    margin-top: 8px;
    font-family: "Montserrat", sans-serif;
    font-weight: 600;
    font-size: 8.5px;
    letter-spacing: 0.2px;
    color: var(--grey);
  }
  .web {
    position: absolute;
    left: 0;
    right: 0;
    top: 147px;
    text-align: center;
    font-family: "Poppins", sans-serif;
    font-weight: 600;
    font-size: 24px;
    letter-spacing: 5px;
    color: var(--ink);
  }
  .web__domain { color: var(--orange-deep); }
</style>
</head>
<body>
<main class="canvas">
  <section class="billboard" aria-label="Velmora billboard">
    <svg class="billboard__bands" viewBox="0 0 1621 323" preserveAspectRatio="none" aria-hidden="true">
      <defs>
        <linearGradient id="band-left" x1="0" y1="1" x2="1" y2="0">
          <stop offset="0" stop-color="var(--orange)"/>
          <stop offset="0.55" stop-color="#F9C76E"/>
          <stop offset="1" stop-color="var(--orange-soft)"/>
        </linearGradient>
        <linearGradient id="band-right" x1="0" y1="0" x2="1" y2="1">
          <stop offset="0" stop-color="#FCC451"/>
          <stop offset="0.6" stop-color="var(--orange)"/>
          <stop offset="1" stop-color="var(--orange-deep)"/>
        </linearGradient>
        <linearGradient id="wash" x1="0" y1="0" x2="1" y2="0">
          <stop offset="0" stop-color="var(--paper)"/>
          <stop offset="0.5" stop-color="var(--white)"/>
          <stop offset="1" stop-color="var(--paper)"/>
        </linearGradient>
      </defs>
      <rect width="1621" height="323" fill="url(#wash)"/>
      <polygon points="0,0 66,0 536,323 0,323" fill="url(#band-left)"/>
      <polygon points="0,120 0,323 330,323" fill="var(--orange)" opacity="0.35"/>
      <polygon points="1076,0 1621,0 1621,323 1546,323" fill="url(#band-right)"/>
      <polygon points="1260,0 1621,0 1621,250" fill="var(--orange-deep)" opacity="0.25"/>
    </svg>

    <div class="brand">
      <div class="brand__row">
        <span class="brand__square" aria-hidden="true"></span>
        <span class="brand__name">VELMORA</span>
      </div>
      <p class="brand__tagline">IZVOĐENJE I VOĐENJE GRAĐEVINSKIH RADOVA</p>
    </div>

    <p class="web">www.<span class="web__domain">velmora</span>.hr</p>
  </section>
</main>
</body>
</html>
```